Young judge needs a website to publish and to connect

I would like to have a website where I can publish my articles in public law. I am judge at the Alpine Civic Review Tribunal. Therefore, the website must have a calm, friendly and fairly neutral design. Also, it should be mobile friendly and easy to use.

On my website, I want to

- publish articles such as https://www.brindlepost.example/pulse/how-win-court-tobias-wenger/ and get feedbacks from my colleagues
- generate interest for my project on 'Statutes and Society - Notes from the Chamber', a book that I would like to publish in 2020 and which brings together my publications on public law (http://www.civicnorm.example/content/english/profil/publikationen.html ).
- provide updates for my university courses on constitutional, administrative and international law.

For that purpose, I would kindly ask you to suggest a website that communicates a fresh approach to the work of a young judge in constitutional and administrative law. Please have in mind that I do not only sit on the bench, but that I also work in academia. Therefore, it should be suitable for an audience from both university and law practice. The website should replace the existing website on www.civicnorm.example that I designed when still working as a lawyer. Thank you.

Target Market(s)

Academica, law firms, courts

Industry/Entity Type

University

Contact Information for Business Card

Tobias Wenger
Judge
Alpine Civic Review Tribunal
M +41 79 5XX 8X 2X

Logo Text

Notes from the Chamber

Number of Pages Required

5+ page

Font styles to use
Sans Serif

Colors
0455a3

Requirements
Must have
• - a page where I can publish and get feedbacks
• - a page about my project on law and politics
• - a page where I can provide updates for my university courses on constitutional, administrative and international law
• - page where I can list current and planned projects
• - a collaborative, young and fresh approach
Nice to have
• - a page reserved for my colleagues at the Alpine Civic Review Tribunal where I can alert them about to possibility to collaborate (if possibly password protected) and where they may suggest what to contribute to a specific project
Should not have
• anything which might to suggest that I want to make money with it, bragging or pretentious. Do not forget: I am judge, not a barrister.

```html
<!DOCTYPE html>
<html lang="en">
<head>
<meta charset="utf-8">
<title>Tobias Wenger — Notes from the Chamber</title>
<link href="https://fonts.googleapis.com/css2?family=Open+Sans:ital,wght@0,300;0,400;0,600;0,700;1,400&display=swap" rel="stylesheet">
<style>
:root{
  --blue:#2c509f;
  --blue-light:#3e6fd0;
  --ink:#1b1b1b;
  --text:#444;
  --line:#d4d4d4;
  --black:#0c0c0c;
  --panel:#141414;
  --band:#dcdcdc;
  --white:#fff;
}
*{box-sizing:border-box;margin:0;padding:0}
html,body{width:1200px;height:2932px;overflow:hidden;background:var(--white)}
body{font-family:"Open Sans",Arial,sans-serif;color:var(--text)}
.page{position:relative;width:1200px;height:2932px;overflow:hidden}
.abs{position:absolute}

/* top bar */
.topbar{left:0;top:0;width:1200px;height:39px;background:var(--black);z-index:3}
.topbar .links{position:absolute;right:244px;top:12px;font-size:10px;color:#ccc;display:flex;gap:22px}
.topbar .links span::before{content:"";display:inline-block;width:7px;height:7px;border:1px solid #aaa;border-radius:50%;margin-right:6px;vertical-align:-1px}
.topbar .contact{position:absolute;right:50px;top:6px;height:27px;padding:0 14px;background:#2a2a2a;color:#ddd;font-size:10px;line-height:27px}

/* hero */
.hero{left:0;top:0;width:1200px;height:674px;background:radial-gradient(ellipse at 66% 42%,#6c5a4a 0%,#3c332c 32%,#1d1a18 62%,#111 100%)}
.header{left:0;top:39px;width:1200px;height:90px;background:rgba(0,0,0,.35);z-index:2}
.brand{position:absolute;left:78px;top:26px;display:flex;align-items:center;gap:12px}
.brand .mark{width:30px;height:30px;background:var(--blue)}
.brand .name{font-size:27px;font-weight:700;color:var(--white);letter-spacing:.5px}
.nav{position:absolute;left:461px;top:0;display:flex;height:90px}
.nav a{display:block;height:90px;line-height:90px;padding:0 14px;color:var(--white);font-size:13px;text-decoration:none;font-weight:600;white-space:nowrap}
.nav a.active{background:var(--blue);width:98px;text-align:center}
.nav a.dd::after{content:"";display:inline-block;width:5px;height:5px;border-right:1px solid #fff;border-bottom:1px solid #fff;transform:rotate(45deg);margin-left:7px;vertical-align:3px}
.slogan{left:76px;top:326px;color:var(--white);font-size:37px;font-weight:300;letter-spacing:-.5px}
.subslogan{left:78px;top:386px;color:var(--white);font-size:20px;letter-spacing:1.5px}
.btn{height:36px;line-height:34px;font-size:13px;text-align:center;color:var(--white);letter-spacing:.5px}
.btn.primary{left:78px;top:443px;width:149px;background:var(--blue);border:1px solid var(--blue)}
.btn.ghost{left:236px;top:443px;width:155px;border:2px solid #fff;line-height:32px}
.arrow{width:28px;height:34px;background:rgba(0,0,0,.45);display:flex;align-items:center;justify-content:center}

/* feedback + about */
.feedback{left:78px;top:575px;width:352px;height:337px;background:var(--panel)}
.feedback h2{height:72px;line-height:72px;text-align:center;color:var(--white);font-weight:400;font-size:25px;border-bottom:1px solid #333}
.feedback h2 em{font-style:normal;color:var(--blue-light)}
.feedback .field{position:absolute;left:32px;width:293px;height:25px;background:#2b2b2b;color:#888;font-size:9px;line-height:25px;padding-left:8px}
.feedback .submit{position:absolute;left:32px;top:253px;width:293px;height:36px;background:var(--blue);color:var(--white);font-size:12px;text-align:center;line-height:36px}
.about{left:432px;top:575px;width:693px;height:337px;background:var(--white);border:1px solid #e2e2e2}
.about h2{position:absolute;left:20px;top:22px;font-size:27px;font-weight:400;color:var(--ink)}
.about .rule{position:absolute;left:20px;top:68px;width:66px;height:3px;background:var(--blue)}
.about p{position:absolute;left:20px;top:90px;width:652px;font-size:12.6px;line-height:21px;text-align:justify;color:#333}

/* section headings */
.sec-title{font-size:21px;font-weight:400;color:var(--ink)}
.sec-line{height:1px;background:#bbb}
.viewall{left:1008px;top:988px;width:117px;height:33px;border:1px solid #ccc;display:flex;font-size:11px;color:#333}
.viewall span{flex:1;text-align:center;line-height:31px;border-right:1px solid #ccc}
.viewall i{width:34px;display:flex;align-items:center;justify-content:center}

/* cards */
.card{top:1063px;height:379px;border:1px solid #ddd;background:var(--white)}
.card .photo{height:223px}
.card .title{height:80px;background:var(--black);color:var(--white);padding:14px 18px}
.card .title.blue{background:var(--blue)}
.card .title small{display:block;font-size:10px;color:#ddd}
.card .title b{display:block;font-size:17px;font-weight:400;margin-top:2px;white-space:nowrap}
.card .details{height:41px;line-height:41px;background:#d2d2d2;padding-left:18px;font-size:13px;color:#333}
.card .meta{height:33px;line-height:33px;padding-left:18px;font-size:10.5px;color:#333;display:flex;gap:18px;white-space:nowrap}
.card .meta span{display:flex;align-items:center;gap:7px}
.projects{left:879px;top:1063px;width:246px;height:379px;background:linear-gradient(180deg,#1a1613,#2d241f 60%,#15110f)}
.projects h3{position:absolute;left:30px;top:18px;color:var(--white);font-weight:400;font-size:16px}
.projects ul{position:absolute;left:30px;top:70px;width:190px;list-style:none}
.projects li{height:48px;line-height:44px;font-size:10.5px;color:#bbb;border-bottom:2px solid #ddd}
.projects li.on{color:var(--blue-light)}
.sidearrow{top:1240px;width:14px;height:20px}

/* areas of work */
.area{width:400px}
.area .icon{position:absolute;left:0;top:0;width:70px;height:70px;border:1px solid #ccc;border-radius:50%;display:flex;align-items:center;justify-content:center;background:var(--white)}
.area h4{position:absolute;left:92px;top:-12px;font-size:17px;font-weight:400;color:#444;white-space:nowrap}
.area p{position:absolute;left:92px;top:16px;width:380px;font-size:12.4px;line-height:20px;color:#333}

/* about me */
.portrait{left:78px;top:1925px;width:399px;height:400px;background:linear-gradient(180deg,#8d8f93,#6b6e74 55%,#2b3242)}
.aboutme h2{position:absolute;left:528px;top:1922px;font-size:29px;font-weight:400;color:var(--ink)}
.aboutme .rule{position:absolute;left:528px;top:1974px;width:66px;height:3px;background:var(--blue)}
.aboutme .lead{position:absolute;left:518px;top:2007px;width:520px;font-style:italic;font-size:13px;line-height:21px;color:#333}
.aboutme .body{position:absolute;left:516px;top:2074px;width:590px;font-size:13px;line-height:21px;color:#333}
.stats-line{left:516px;top:2198px;width:609px;height:1px;background:#ddd}
.stat{top:2214px;width:160px;text-align:center}
.stat .num{font-size:16px;color:#333;margin-top:14px}
.stat .lbl{font-size:12px;color:#555;margin-top:13px;letter-spacing:.3px}

/* colleague notes band */
.notes{left:0;top:2405px;width:1200px;height:256px;background:var(--band)}
.notebox{left:295px;top:2458px;width:610px;height:151px;background:var(--white);border:1px solid #cfcfcf}
.notebox p{position:absolute;left:60px;top:40px;width:510px;font-style:italic;font-size:10.5px;line-height:15px;color:#333}
.qmark{font-family:Georgia,serif;font-size:64px;color:#e4e4e4;line-height:1}
.nsq{width:36px;height:36px;background:var(--white);top:2517px}

/* footer */
.footer{left:0;top:2661px;width:1200px;height:271px;background:linear-gradient(90deg,#121212,#1c1c1c 60%,#2a2724)}
.footer .brand{left:78px;top:60px}
.footer .brand .name{font-size:24px}
.fcol-title{font-size:12px;color:#ddd;letter-spacing:.5px}
.fline{height:1px;background:#333}
.ftext{font-size:9px;line-height:14px;color:#8a8a8a}
.fmenu{list-style:none;font-size:9.5px;color:#ccc;line-height:16px}
.fmenu li::after{content:"›";margin-left:14px;color:#aaa}
.contact-photo{width:72px;height:75px;background:linear-gradient(180deg,#6b5447,#b79c8c 55%,#e8e3de)}
.social{display:flex;gap:22px}
.social span{width:12px;height:12px;border-radius:50%;background:#e5e5e5;display:block}
</style>
</head>
<body>
<div class="page">

  <!-- HERO -->
  <div class="abs hero" role="img" aria-label="Portrait photograph of a bearded man in a dark suit, dim warm background"></div>
  <div class="abs topbar">
    <div class="links"><span>Signin</span><span>Register</span></div>
    <div class="contact">Mobile: +41 79 5XX 8X 2X</div>
  </div>
  <header class="abs header">
    <div class="brand"><div class="mark"></div><div class="name">TOBIAS WENGER</div></div>
    <nav class="nav">
      <a class="active">HOME</a>
      <a class="dd">ARTICLES</a>
      <a class="dd">BOOK</a>
      <a class="dd">COURSES</a>
      <a class="dd">PROJECTS</a>
      <a class="dd">BLOG</a>
      <a>CONTACT</a>
    </nav>
  </header>
  <div class="abs slogan">Lorem Ipsum is simply</div>
  <div class="abs subslogan">A GOOD SLOGAN HERE</div>
  <div class="abs btn primary">READ ARTICLES</div>
  <div class="abs btn ghost">KNOW MORE</div>
  <div class="abs arrow" style="left:12px;top:383px"><svg width="8" height="12"><path d="M7 1 2 6l5 5" stroke="#ccc" fill="none" stroke-width="1.5"/></svg></div>
  <div class="abs arrow" style="left:1160px;top:383px"><svg width="8" height="12"><path d="M1 1l5 5-5 5" stroke="#ccc" fill="none" stroke-width="1.5"/></svg></div>

  <!-- FEEDBACK + ABOUT -->
  <section class="abs feedback">
    <h2>SHARE <em>YOUR</em> FEEDBACK</h2>
    <div class="field" style="top:104px">Your Name*</div>
    <div class="field" style="top:149px">Your mail*</div>
    <div class="field" style="top:194px">Your comment*</div>
    <div class="submit">SEND FEEDBACK</div>
  </section>
  <section class="abs about">
    <h2>ABOUT CIVICNORM.EXAMPLE</h2>
    <div class="rule"></div>
    <p>civicnorm.example is the personal website of Tobias Wenger, a judge at the Alpine Civic Review Tribunal specialising in judicial review of administrative action and administrative procedure. Here he publishes articles on public law and invites colleagues from courts, universities and practice to share their feedback. His particular interest lies in health and higher education matters, but he also writes on other questions of constitutional and administrative law. He teaches constitutional and administrative law at Lakeside University, where he is currently completing his post-doctoral thesis.</p>
  </section>

  <!-- KEY FEATURES -->
  <div class="abs sec-title" style="left:76px;top:998px">Key Features</div>
  <div class="abs sec-line" style="left:212px;top:1020px;width:796px"></div>
  <div class="abs viewall"><span>View All</span><i><svg width="7" height="11"><path d="M1 1l5 4.5L1 10" stroke="#999" fill="none"/></svg></i></div>
  <svg class="abs sidearrow" style="left:32px" viewBox="0 0 14 20"><path d="M10 2 3 10l7 8" stroke="#999" fill="none" stroke-width="1.5"/></svg>
  <svg class="abs sidearrow" style="left:1156px" viewBox="0 0 14 20"><path d="M4 2l7 8-7 8" stroke="#999" fill="none" stroke-width="1.5"/></svg>

  <article class="abs card" style="left:78px;width:244px">
    <div class="photo" role="img" aria-label="Photograph of men in dark suits walking together" style="background:linear-gradient(180deg,#cfcdc9,#6a6866 55%,#2a2a2e)"></div>
    <div class="title blue"><small>publish article</small><b>How to win in Court</b></div>
    <div class="details">DETAILS</div>
    <div class="meta"><span><svg width="10" height="10"><circle cx="5" cy="3" r="2.5" fill="#333"/><path d="M0 10a5 4 0 0 1 10 0z" fill="#333"/></svg>By T. WENGER</span><span><svg width="12" height="10"><ellipse cx="6" cy="5" rx="5.5" ry="4" fill="none" stroke="#333" stroke-width="1.5"/></svg>0 comment</span></div>
  </article>
  <article class="abs card" style="left:342px;width:246px">
    <div class="photo" role="img" aria-label="Photograph of a hand writing with a pen on paper" style="background:linear-gradient(160deg,#f2f2f2,#d9d6d2 55%,#b9b4ae)"></div>
    <div class="title"><small>book project</small><b>Statutes and Society</b></div>
    <div class="details">DETAILS</div>
    <div class="meta"><span><svg width="10" height="10"><circle cx="5" cy="3" r="2.5" fill="#333"/><path d="M0 10a5 4 0 0 1 10 0z" fill="#333"/></svg>By T. WENGER</span><span><svg width="12" height="10"><ellipse cx="6" cy="5" rx="5.5" ry="4" fill="none" stroke="#333" stroke-width="1.5"/></svg>0 comment</span></div>
  </article>
  <article class="abs card" style="left:614px;width:244px">
    <div class="photo" role="img" aria-label="Photograph of a person reviewing printed documents" style="background:linear-gradient(160deg,#e9ecef,#c6ccd3 50%,#3d4452)"></div>
    <div class="title"><small>updates</small><b>My University Courses</b></div>
    <div class="details">DETAILS</div>
    <div class="meta"><span><svg width="10" height="10"><circle cx="5" cy="3" r="2.5" fill="#333"/><path d="M0 10a5 4 0 0 1 10 0z" fill="#333"/></svg>By T. WENGER</span><span><svg width="12" height="10"><ellipse cx="6" cy="5" rx="5.5" ry="4" fill="none" stroke="#333" stroke-width="1.5"/></svg>0 comment</span></div>
  </article>
  <aside class="abs projects" role="img" aria-label="Dark study room background with list of projects">
    <h3>My projects</h3>
    <ul>
      <li class="on">CURRENT PROJECTS</li>
      <li>PLANNED PROJECTS</li>
      <li>BOOK PROJECT</li>
      <li>COLLEAGUES' AREA</li>
      <li>UNIVERSITY COURSES</li>
    </ul>
  </aside>

  <!-- AREAS OF WORK -->
  <div class="abs sec-title" style="left:76px;top:1528px">Areas of Work</div>
  <div class="abs sec-line" style="left:228px;top:1550px;width:897px"></div>

  <div class="abs area" style="left:102px;top:1628px">
    <div class="icon"><svg width="26" height="22" viewBox="0 0 26 22"><path d="M3 8h5l9-6v18l-9-6H3z" fill="none" stroke="#2c509f" stroke-width="1.6"/><path d="M20 7q3 4 0 8M22 4q6 7 0 14" fill="none" stroke="#2c509f" stroke-width="1.4"/></svg></div>
    <h4>CONSTITUTIONAL LAW</h4>
    <p>Lorem ipsum dolor sit amet, consectetur adipiscing elit. Donec dui augue, aliquam ut metus in, malesuada ornare nisl. Aenean nec tincidunt ligula. Fusce ac sem leo.</p>
  </div>
  <div class="abs area" style="left:639px;top:1628px">
    <div class="icon"><svg width="26" height="26" viewBox="0 0 26 26"><circle cx="13" cy="13" r="11" fill="none" stroke="#2c509f" stroke-width="1.6"/><ellipse cx="13" cy="13" rx="5" ry="11" fill="none" stroke="#2c509f" stroke-width="1.4"/><path d="M2 13h22M4 7h18M4 19h18" stroke="#2c509f" stroke-width="1.3"/></svg></div>
    <h4>INTERNATIONAL LAW</h4>
    <p>Lorem ipsum dolor sit amet, consectetur adipiscing elit. Donec dui augue, aliquam ut metus in, malesuada ornare nisl. Aenean nec tincidunt ligula. Fusce ac sem leo.</p>
  </div>
  <div class="abs area" style="left:102px;top:1760px">
    <div class="icon"><svg width="22" height="26" viewBox="0 0 22 26"><path d="M2 2h12l6 6v16H2z" fill="none" stroke="#2c509f" stroke-width="1.6"/><path d="M6 12h10M6 16h10M6 20h7" stroke="#2c509f" stroke-width="1.4"/></svg></div>
    <h4>ADMINISTRATIVE LAW</h4>
    <p>Lorem ipsum dolor sit amet, consectetur adipiscing elit. Donec dui augue, aliquam ut metus in, malesuada ornare nisl. Aenean nec tincidunt ligula. Fusce ac sem leo.</p>
  </div>
  <div class="abs area" style="left:639px;top:1760px">
    <div class="icon"><svg width="28" height="26" viewBox="0 0 28 26"><path d="M14 2v22M8 24h12M4 6h20" stroke="#2c509f" stroke-width="1.6" fill="none"/><path d="M4 6l-3 8h6zM24 6l-3 8h6z" fill="none" stroke="#2c509f" stroke-width="1.4"/></svg></div>
    <h4>COLLABORATIVE PROJECTS</h4>
    <p>Lorem ipsum dolor sit amet, consectetur adipiscing elit. Donec dui augue, aliquam ut metus in, malesuada ornare nisl. Aenean nec tincidunt ligula. Fusce ac sem leo.</p>
  </div>

  <!-- ABOUT ME -->
  <div class="abs portrait" role="img" aria-label="Portrait photograph of a smiling man in a navy suit and tie"></div>
  <section class="aboutme">
    <h2>ABOUT ME</h2>
    <div class="rule"></div>
    <p class="lead">Lorem ipsum dolor sit amet, consectetur adipiscing elit, sed do eiusmod tempor incididunt ut labore et dolore magna aliqua</p>
    <p class="body">Neque porro quisquam est, qui dolorem ipsum quia dolor sit amet, consectetur, adipisci velit, sed quia non numquam eius modi tempora incidunt ut labore et dolore magnam aliquam quaerat voluptatem. Ut enim ad minima veniam, quis nostrum exercitationem ullam corporis suscipit laboriosam.</p>
  </section>
  <div class="abs stats-line"></div>
  <div class="abs stat" style="left:540px">
    <svg width="30" height="28" viewBox="0 0 30 28"><path d="M7 2h12l5 5v19H7z" fill="none" stroke="#2c509f" stroke-width="1.8"/><path d="M11 12h9M11 16h9M11 20h6" stroke="#2c509f" stroke-width="1.6"/></svg>
    <div class="num">Articles</div><div class="lbl">READ &amp; COMMENT</div>
  </div>
  <div class="abs stat" style="left:716px">
    <svg width="30" height="28" viewBox="0 0 30 28"><circle cx="15" cy="8" r="6" fill="none" stroke="#2c509f" stroke-width="1.8"/><path d="M4 26q1-10 11-10t11 10z" fill="none" stroke="#2c509f" stroke-width="1.8"/></svg>
    <div class="num">Colleagues</div><div class="lbl">COLLABORATE</div>
  </div>
  <div class="abs stat" style="left:916px">
    <svg width="30" height="28" viewBox="0 0 30 28"><circle cx="15" cy="14" r="5" fill="none" stroke="#2c509f" stroke-width="1.8"/><circle cx="15" cy="14" r="10" fill="none" stroke="#2c509f" stroke-width="3" stroke-dasharray="4 3.85"/></svg>
    <div class="num">Courses</div><div class="lbl">STAY UPDATED</div>
  </div>

  <!-- COLLEAGUE NOTES -->
  <div class="abs notes"></div>
  <svg class="abs" style="left:126px;top:2525px" width="10" height="18"><path d="M8 1 2 9l6 8" stroke="#888" fill="none" stroke-width="1.5"/></svg>
  <div class="abs nsq" style="left:168px"></div>
  <svg class="abs" style="left:956px;top:2525px" width="10" height="18"><path d="M2 1l6 8-6 8" stroke="#888" fill="none" stroke-width="1.5"/></svg>
  <div class="abs nsq" style="left:996px"></div>
  <div class="abs notebox">
    <div class="abs qmark" style="left:12px;top:4px">&ldquo;</div>
    <p>Lorem Ipsum is simply dummy text of the printing and typesetting industry. Lorem Ipsum has been the industry's standard dummy text ever since the 1500s, when an unknown printer took a galley of type and scrambled it to make a type specimen book.</p>
    <div class="abs qmark" style="left:268px;top:92px">&rdquo;</div>
  </div>

  <!-- FOOTER -->
  <footer class="abs footer">
    <div class="brand"><div class="mark"></div><div class="name">TOBIAS WENGER</div></div>
    <div class="abs fline" style="left:78px;top:116px;width:210px"></div>
    <p class="abs ftext" style="left:78px;top:148px;width:210px;text-align:justify">Lorem ipsum is simply dummy text of the printing and typesetting industry. Lorem ipsum has been the industry's standard dummy text ever since the 1500s, when an unknown printer took a galley of type and scrambled it to make a type specimen book.</p>

    <div class="abs fcol-title" style="left:385px;top:64px">MENU</div>
    <div class="abs fline" style="left:385px;top:116px;width:150px"></div>
    <ul class="abs fmenu" style="left:385px;top:142px">
      <li>Home</li><li>ARTICLES</li><li>BOOK</li><li>COURSES</li><li>CONTACT</li>
    </ul>

    <div class="abs fcol-title" style="left:600px;top:64px">CONTACT INFO</div>
    <div class="abs fline" style="left:600px;top:116px;width:236px"></div>
    <div class="abs contact-photo" style="left:600px;top:140px" role="img" aria-label="Small portrait photograph"></div>
    <div class="abs" style="left:686px;top:144px;font-size:9.5px;color:#ddd">Tobias Wenger <span style="color:#999">(Judge)</span></div>
    <p class="abs ftext" style="left:686px;top:162px;width:150px">Alpine Civic Review Tribunal. M +41 79 5XX 8X 2X. Lecturer in public law at Lakeside University.</p>

    <div class="abs fcol-title" style="left:948px;top:64px">FOLLOW US</div>
    <div class="abs fline" style="left:948px;top:116px;width:177px"></div>
    <p class="abs ftext" style="left:948px;top:148px;width:177px;color:#555">Lorem ipsum is simply dummy text of the printing and typesetting industry.</p>
    <div class="abs social" style="left:956px;top:212px" aria-label="Social links">
      <span></span><span></span><span></span><span></span><span></span>
    </div>
  </footer>

</div>
</body>
</html>
```